Medical centre needs a business card

We are a medcial centre in Australia, needing a new business card. Our demographic is low working class families. We are going to be renovating our premises to modernise the look and also had a new logo done a few months ago representing quality and community, and now need to update our cards. It needs to be doubled sided, with logo and contact details on the front, and appointment details on the back. . Needs to be modern and simple, easy to read. <br/><br/>Name: Fern Vale Medical Centre <br/>Address: 512 Kestrel Rd (Cnr Kestrel Rd & Lindon Park Rd),<br/>Corvane Court Shopping Centre, Marlow Downs, WA 6999<br/>Ph: 08 8361 4027<br/>Tag line: Where every visit counts for you<br/>Website: www.fernvalemedicalcentre.example.au<br/>Online bookings also available<br/><br/>(On the back, to have 3 lines of appointments that can be written in.<br/>Day, date, time)<br/><br/>Your next appointment is on<br/>Can try “M T W Th F Sa Su _________________ at ____________ am/pm” or other combinations <br/>Please advise as soon as possible if unable to attend<br/>Cancellation fees apply if less than 2 hrs notice<br/>Online appointments available (please highlight this option by either by position, colour or font)

Target Market(s)

Lower social economic working class, young families to seniors

Industry/Entity Type

Medical Centre

Contact Information for Business Card

Fern Vale Medical Centre
512 Kestrel Rd (Cnr Kestrel Rd & Lindon Park Drive)
Corvane Court Shopping Centre
Marlow Downs WA 6999
Ph: 08 8361 4027
www.fernvalemedicalcentre.example.au
Tagline line: where every visit counts for you
Back side is for appointments
Your next appointment is with Dr ______________
Day/date/time (Please give 3 lines of appointments)
Please advise as soon as possible if unable to attend
Cancellation fees apply if less than 2 hours notice
Online appointments available
Book online easily and conveniently (please highlight online appointments)

Font styles to use
Serif
Sans Serif

Colors

Designer to choose colors to be used in the design.

Requirements
Must have
• Modern and simple
• Easy to ready
• Induces a wellbeing feeling
• Incorporate our logo colours and feel from logo
• Induces feeling of stability and security
Nice to have
• Attract attention
• Pleasant to look at
• Feeling of innovation
Should not have
• Loud clashing colours
• Overly luxurious feeling
• Overly artistic

```html
<!DOCTYPE html>
<html lang="en">
<head>
<meta charset="utf-8">
<title>Fern Vale Medical Centre – Business Card</title>
<link rel="stylesheet" href="https://fonts.googleapis.com/css2?family=Lato:wght@300;400&display=swap">
<style>
  :root {
    --blue-deep: #0f6db5;
    --blue-bright: #27abe2;
    --blue-brand: #1a7cc1;
    --green: #8dc63f;
    --green-title: #b9d63a;
    --paper: #f3f3f5;
    --ink: #3a3a3a;
    --faint: #c8d8ec;
    --stage: #1f1f21;
  }
  * { margin: 0; padding: 0; box-sizing: border-box; }
  html, body { width: 1131px; height: 1200px; overflow: hidden; }
  body {
    position: relative;
    background: var(--stage);
    font-family: "Lato", sans-serif;
    color: var(--ink);
  }
  .card {
    position: absolute;
    left: 153px;
    width: 781px;
    height: 447px;
    border-radius: 24px;
    overflow: hidden;
    background: var(--paper);
  }
  .card-front { top: 109px; }
  .card-back { top: 599px; }

  /* Front */
  .front-panel {
    position: absolute;
    left: 0; top: 0;
    width: 397px; height: 100%;
    background: linear-gradient(90deg, var(--blue-deep), var(--blue-bright));
    color: #fff;
  }
  .tagline {
    position: absolute;
    left: 0; top: 72px;
    width: 389px;
    text-align: center;
    font-weight: 300;
    font-size: 30px;
    line-height: 39px;
  }
  .contact-list {
    position: absolute;
    left: 32px; top: 352px;
    list-style: none;
    font-weight: 300;
    font-size: 17.5px;
  }
  .contact-list li {
    display: flex;
    align-items: center;
    height: 24px;
    margin-bottom: 8px;
  }
  .contact-icon {
    width: 23px; height: 23px;
    background: var(--green);
    margin-right: 16px;
    display: flex; align-items: center; justify-content: center;
  }
  .brand {
    position: absolute;
    left: 397px; top: 66px;
    width: 384px;
    display: flex; align-items: center; justify-content: center;
  }
  .brand-dot {
    width: 34px; height: 34px;
    border-radius: 50%;
    background: var(--blue-brand);
    margin-right: 14px;
  }
  .brand-name {
    font-weight: 400;
    font-size: 31px;
    line-height: 36px;
    color: var(--blue-brand);
    text-align: center;
  }
  .pin {
    position: absolute;
    left: 566px; top: 237px;
  }
  .address {
    position: absolute;
    left: 397px; top: 314px;
    width: 384px;
    text-align: center;
    font-style: normal;
    font-weight: 400;
    font-size: 17px;
    line-height: 22px;
    color: var(--ink);
  }

  /* Back */
  .back-header {
    position: absolute;
    left: 0; top: 0;
    width: 100%; height: 105px;
    background: linear-gradient(90deg, var(--blue-deep), var(--blue-bright));
    display: flex; align-items: center; justify-content: center;
  }
  .back-title {
    font-weight: 300;
    font-size: 28px;
    color: var(--green-title);
  }
  .appointment-fields {
    position: absolute;
    left: 53px; top: 138px;
    list-style: none;
    font-size: 16.5px;
    font-weight: 400;
  }
  .appointment-fields li {
    display: flex;
    align-items: flex-end;
    height: 26px;
    margin-bottom: 38px;
  }
  .field-label { width: 52px; }
  .write-line {
    width: 354px;
    border-bottom: 2px dotted #555;
    margin-bottom: 6px;
  }
  .attendance-note {
    position: absolute;
    left: 53px; top: 307px;
    font-size: 16px;
    line-height: 21px;
  }
  .brand-faint {
    position: absolute;
    left: 500px; top: 230px;
    width: 260px;
    display: flex; align-items: center; justify-content: center;
  }
  .brand-faint .brand-dot { background: var(--faint); width: 28px; height: 28px; }
  .brand-faint .brand-name { color: var(--faint); font-size: 27px; line-height: 31px; }
  .online-band {
    position: absolute;
    left: 0; top: 374px;
    width: 100%; height: 37px;
    background: linear-gradient(90deg, var(--blue-deep), var(--blue-bright));
    color: #fff;
    font-weight: 300;
    font-size: 17.5px;
    display: flex; align-items: center; justify-content: center;
  }
</style>
</head>
<body>

<section class="card card-front" aria-label="Card front">
  <div class="front-panel">
    <p class="tagline">where every visit<br>counts for you</p>
    <ul class="contact-list">
      <li>
        <span class="contact-icon">
          <svg width="15" height="15" viewBox="0 0 24 24" aria-hidden="true"><path fill="#fff" d="M6.6 10.8a15.1 15.1 0 0 0 6.6 6.6l2.2-2.2a1 1 0 0 1 1-.25 11.4 11.4 0 0 0 3.6.57 1 1 0 0 1 1 1V20a1 1 0 0 1-1 1A17 17 0 0 1 3 4a1 1 0 0 1 1-1h3.5a1 1 0 0 1 1 1c0 1.25.2 2.45.57 3.57a1 1 0 0 1-.25 1z"/></svg>
        </span>
        08 8361 4027
      </li>
      <li>
        <span class="contact-icon"></span>
        fernvalemedicalcentre.example.au
      </li>
    </ul>
  </div>

  <div class="brand">
    <span class="brand-dot"></span>
    <span class="brand-name">Fern Vale<br>Medical Centre</span>
  </div>

  <svg class="pin" width="34" height="54" viewBox="0 0 34 54" aria-hidden="true">
    <path fill="var(--blue-brand)" d="M17 0C7.6 0 0 7.6 0 17c0 12.5 17 37 17 37s17-24.5 17-37C34 7.6 26.4 0 17 0z"/>
    <circle cx="17" cy="16" r="6.5" fill="#fff"/>
  </svg>

  <address class="address">
    Fern Vale Medical Centre<br>
    512 Kestrel Rd Corvane Court<br>
    Shopping Centre Marlow Downs<br>
    WA 6999
  </address>
</section>

<section class="card card-back" aria-label="Card back">
  <header class="back-header">
    <h2 class="back-title">Your next appointment</h2>
  </header>

  <ul class="appointment-fields">
    <li><span class="field-label">Dr</span><span class="write-line"></span></li>
    <li><span class="field-label">Date</span><span class="write-line"></span></li>
    <li><span class="field-label">Time</span><span class="write-line"></span></li>
  </ul>

  <p class="attendance-note">as soon as possible if unable to attend Cancellation<br>fees apply if less than 2 hours notice</p>

  <div class="brand-faint" aria-hidden="true">
    <span class="brand-dot"></span>
    <span class="brand-name">Fern Vale<br>Medical Centre</span>
  </div>

  <p class="online-band">Online appointments available Book online easily and conveniently</p>
</section>

</body>
</html>
```